Internet of Things integrator needs logo and website design

We need a logo and website design for our company ("Brightwave Link"). We integrate IoT(Internet of Things) projects including: devices, network and sw solutions for all type of vertical markets. The image should be professional like the following site: quorvel.io clear and easy surfing, and should include about the same sections shown in that website (Why Us?, Products, Resources, Company, etc). Website colors should follow logo colors (logo has to be designed and aproved first). The logo should be something like the one used at tandemvexa.com (image attached), where we could use the logo to susbtitute the letter "o" in "IoT". The final design should communicate professionalism and experience.

Coding

Coded - Design and coding required

Number of Pages Required

5+ page

Font styles to use
Other font styles liked:
• see quorvel.io wensite

Requirements
Must have
• Serious and professional look and feel as in: quorvel.io website.
The following pages should be included:
- home page
- Why Us?
- Products
- Resources
- Company
- Newsroom
- Contact
Nice to have
• High tech look and feel
Should not have
• Fun or not serious images (cartoons, etc.)

```html
<!DOCTYPE html>
<html lang="en">
<head>
<meta charset="utf-8">
<title>Contact Us – Brightwave Link</title>
<link rel="stylesheet" href="https://fonts.googleapis.com/css2?family=Poppins:wght@500;600;700;800&family=Roboto:wght@400;500;700&display=swap">
<style>
:root{
  --navy:#0b0b5c;
  --ink:#111;
  --muted:#666;
  --field:#f2f2f2;
  --blue-light:#24a3f8;
  --blue-deep:#1e22a6;
  --icon-bg:#e6f1fa;
  --white:#fff;
}
*{box-sizing:border-box;margin:0;padding:0}
html,body{width:751px;height:1200px;overflow:hidden;background:var(--white)}
body{position:relative;font-family:"Roboto",sans-serif;color:var(--ink)}
.abs{position:absolute}
.brand{font-family:"Poppins",sans-serif;font-weight:600;letter-spacing:-.3px;white-space:nowrap}
.header-brand{left:56px;top:14px;font-size:18px;color:var(--blue-deep);line-height:28px}
.nav{left:273px;top:14px;display:flex;gap:21px;font-size:10.5px;font-weight:500;line-height:28px}
.nav a{color:var(--ink);text-decoration:none}
.nav a.dim{color:#444}
.btn-grad{background:linear-gradient(90deg,var(--blue-light),var(--blue-deep));color:var(--white);border-radius:20px;display:flex;align-items:center;justify-content:center;font-weight:700}
.header-cta{left:603px;top:15px;width:92px;height:28px;font-family:"Poppins",sans-serif;font-size:9px;letter-spacing:.1px}
.page-title{left:0;width:751px;top:115px;text-align:center;font-family:"Poppins",sans-serif;font-weight:700;font-size:27px;color:var(--navy)}
.crumb{left:0;width:751px;top:147px;text-align:center;font-size:11px}
.section-title{left:0;width:751px;top:241px;text-align:center;font-family:"Poppins",sans-serif;font-weight:700;font-size:22px;color:var(--navy)}
.intro{left:0;width:751px;top:279px;text-align:center;font-size:10.5px;line-height:16px;color:#333}
.field{left:191px;width:369px;height:37px;background:var(--field);border-radius:4px;padding:0 14px;font-family:"Poppins",sans-serif;font-weight:500;font-size:11px;color:var(--muted);display:flex;align-items:center}
.field.message{height:99px;align-items:flex-start;padding-top:12px}
.submit{left:310px;top:566px;width:130px;height:32px;font-size:13px}
.info{width:160px;text-align:center}
.info .circle{width:69px;height:69px;border-radius:50%;background:var(--icon-bg);margin:0 auto;display:flex;align-items:center;justify-content:center}
.info h3{margin-top:14px;font-family:"Poppins",sans-serif;font-weight:700;font-size:15.5px;line-height:18px}
.info p{font-size:10.5px;color:#333;margin-top:1px}
.footer-bg{left:0;top:0;width:751px;height:1200px}
.footer-brand{left:56px;top:1025px;font-size:19px;line-height:28px;color:var(--white)}
.fcol{color:var(--white)}
.fcol h4{font-family:"Poppins",sans-serif;font-weight:600;font-size:14px;line-height:18px;margin-bottom:5px}
.fcol ul{list-style:none;font-size:9px;font-weight:500;line-height:18.4px}
.fcol p{font-size:9px;font-weight:500;line-height:18.4px}
.email-input{left:367px;top:1017px;width:154px;height:27px;background:var(--white);border-radius:14px;font-size:9px;color:#333;padding-left:13px;display:flex;align-items:center}
.subscribe{left:370px;top:1049px;width:91px;height:27px;border:1.2px solid var(--white);border-radius:14px;color:var(--white);font-size:10px;font-weight:500;display:flex;align-items:center;justify-content:center}
.map-area{left:526px;top:987px;width:175px;height:103px;background:radial-gradient(ellipse at center,rgba(255,255,255,.1),rgba(255,255,255,0) 70%);border-radius:40px}
.contact-list li{display:flex;align-items:center;gap:6px}
.socials{left:566px;top:1053px;display:flex;gap:11px}
.socials span{width:9px;height:9px;border-radius:50%;background:var(--white)}
.rule{left:56px;top:1168px;width:639px;height:1px;background:rgba(255,255,255,.35)}
.copyright{left:0;width:751px;top:1179px;text-align:center;color:var(--white);font-size:9px;font-weight:500}
.to-top{left:710px;top:1157px;width:21px;height:21px;border-radius:50%;background:var(--white);display:flex;align-items:center;justify-content:center}
</style>
</head>
<body>
<svg class="abs footer-bg" viewBox="0 0 751 1200" aria-hidden="true">
  <defs>
    <linearGradient id="footerGrad" x1="0" y1="0" x2="1" y2="0.3">
      <stop offset="0" stop-color="#24a3f8"/>
      <stop offset="1" stop-color="#1e22a6"/>
    </linearGradient>
  </defs>
  <polygon points="0,893 751,813 751,1200 0,1200" fill="url(#footerGrad)"/>
</svg>

<header>
  <div class="abs brand header-brand">Brightwave Link</div>
  <nav class="abs nav">
    <a href="#">Why Us?</a><a href="#">Products</a><a href="#">Resources</a><a href="#">Company</a><a href="#" class="dim">Newsroom</a>
  </nav>
  <a class="abs btn-grad header-cta">CONTACT US</a>
</header>

<h1 class="abs page-title">CONTACT US</h1>
<div class="abs crumb">Home / Contact Us</div>

<h2 class="abs section-title">GET IN TOUCH WITH US</h2>
<p class="abs intro">You have any query related to our services, just fill out the below form<br>and we will reach out to you on email or over call.</p>

<form>
  <div class="abs field" style="top:329px">Name</div>
  <div class="abs field" style="top:373px">Email</div>
  <div class="abs field" style="top:417px">Phone</div>
  <div class="abs field message" style="top:461px">Message</div>
  <div class="abs btn-grad submit">SUBMIT</div>
</form>

<svg width="0" height="0" style="position:absolute">
  <defs>
    <linearGradient id="iconGrad" x1="0" y1="0" x2="1" y2="1">
      <stop offset="0" stop-color="#24a3f8"/><stop offset="1" stop-color="#1e22a6"/>
    </linearGradient>
  </defs>
</svg>

<div class="abs info" style="left:84px;top:661px">
  <div class="circle"><svg width="24" height="32" viewBox="0 0 24 32"><path d="M12 0C5.4 0 0 5.2 0 11.6 0 19 12 32 12 32s12-13 12-20.4C24 5.2 18.6 0 12 0z" fill="url(#iconGrad)"/><circle cx="12" cy="10" r="4" fill="#fff"/></svg></div>
  <h3>ADDRESS</h3><p>Some goes address here</p>
</div>
<div class="abs info" style="left:295px;top:661px">
  <div class="circle"><svg width="32" height="32" viewBox="0 0 24 24"><path d="M6.6 10.8a15.1 15.1 0 006.6 6.6l2.2-2.2c.3-.3.7-.4 1-.2 1.1.4 2.3.6 3.6.6.6 0 1 .4 1 1V20c0 .6-.4 1-1 1A17 17 0 013 4c0-.6.4-1 1-1h3.5c.6 0 1 .4 1 1 0 1.3.2 2.5.6 3.6.1.3 0 .7-.2 1z" fill="url(#iconGrad)"/></svg></div>
  <h3>PHONE</h3><p>(000) 000-0000</p>
</div>
<div class="abs info" style="left:506px;top:661px">
  <div class="circle"><svg width="28" height="22" viewBox="0 0 28 22"><rect width="28" height="22" rx="2" fill="url(#iconGrad)"/><path d="M2 4l12 8 12-8" stroke="#fff" stroke-width="2" fill="none"/></svg></div>
  <h3>EMAIL</h3><p>hello@bwlink.net</p>
</div>

<footer>
  <div class="abs brand footer-brand">Brightwave Link</div>

  <div class="abs fcol" style="left:241px;top:968px">
    <h4>Useful Links</h4>
    <ul><li>Why Us?</li><li>Products</li><li>Resources</li><li>Company</li><li>Newsroom</li><li>Contact Us</li></ul>
  </div>

  <div class="abs fcol" style="left:367px;top:968px">
    <h4>Newsletter</h4>
    <p>Subscribe to our newsletter</p>
  </div>
  <div class="abs email-input">Email Address</div>
  <div class="abs subscribe">SUBSCRIBE</div>

  <div class="abs map-area" role="img" aria-label="Faint dotted world map decoration"></div>
  <div class="abs fcol contact-list" style="left:566px;top:968px">
    <h4>Contact Us</h4>
    <ul>
      <li><svg width="6" height="8" viewBox="0 0 24 32"><path d="M12 0C5.4 0 0 5.2 0 11.6 0 19 12 32 12 32s12-13 12-20.4C24 5.2 18.6 0 12 0z" fill="#fff"/></svg>Some goes address here</li>
      <li><svg width="7" height="7" viewBox="0 0 24 24"><path d="M6.6 10.8a15.1 15.1 0 006.6 6.6l2.2-2.2c.3-.3.7-.4 1-.2 1.1.4 2.3.6 3.6.6.6 0 1 .4 1 1V20c0 .6-.4 1-1 1A17 17 0 013 4c0-.6.4-1 1-1h3.5c.6 0 1 .4 1 1 0 1.3.2 2.5.6 3.6.1.3 0 .7-.2 1z" fill="#fff"/></svg>+44 ( 2041 ) 873</li>
      <li><svg width="7" height="6" viewBox="0 0 28 22"><rect width="28" height="22" rx="2" fill="#fff"/></svg>hello@bwlink.net</li>
    </ul>
  </div>
  <div class="abs socials"><span></span><span></span><span></span></div>

  <div class="abs rule"></div>
  <div class="abs copyright">Copyright 2020 | All Rights Reserved</div>
  <div class="abs to-top"><svg width="7" height="5" viewBox="0 0 10 6"><path d="M1 5l4-4 4 4" stroke="#1e22a6" stroke-width="1.6" fill="none"/></svg></div>
</footer>
</body>
</html>
```